Business Card Design

Consultation for design, construction athletic facilities specializing in synthetic turf systems and all weather running track systems.
Motto "True Owner Representation"
New Company that we'd like to highlight the LOGO first and foremost with the colors of the background and font as primary colors of the card too if possible. I've also attached a typical larger project design layout that could be used in the background to highlight our design and construction specialty.
Website is something we want very noticeable for driving traffic.
Target Market(s)
Athletic Directors, Designers, Government and Military, Contractors
Industry/Entity Type
Construction
Contact Information for Business Card
Peter L. Vandrell CFB, CTB
48317 W 63rd Ave
Harlow Ridge, WA 99482
C +1 503.555.0147
O +1 808.555.0182
Peter@fieldlaneco.example
www.fieldlaneco.example

```html
<!DOCTYPE html>
<html lang="en">
<head>
<meta charset="utf-8">
<title>Solenne Sport — Business Card</title>
<link rel="stylesheet" href="https://fonts.googleapis.com/css2?family=Exo+2:wght@400;600&display=swap">
<style>
  :root {
    --canvas: #c9c9c7;
    --card-black: #070707;
    --card-white: #f7f6f3;
    --gold: #d9a03a;
    --gold-soft: #c8933a;
  }
  * { margin: 0; padding: 0; box-sizing: border-box; }
  html, body { width: 1200px; height: 1000px; overflow: hidden; }
  body {
    background: var(--canvas);
    font-family: "Exo 2", sans-serif;
    position: relative;
  }
  .card {
    position: absolute;
    left: 215px;
    width: 770px;
    height: 440px;
    background: var(--card-black);
    overflow: hidden;
    box-shadow: 0 6px 18px rgba(0,0,0,0.25);
  }
  .card--front { top: 40px; }
  .card--back { top: 520px; }

  .brand {
    position: absolute;
    display: flex;
    align-items: center;
    gap: 18px;
    color: var(--gold);
    font-weight: 400;
    letter-spacing: 0.14em;
    text-transform: uppercase;
    white-space: nowrap;
  }
  .brand__dot {
    border-radius: 50%;
    background: var(--gold);
    flex: none;
  }
  .card--front .brand { left: 150px; top: 150px; font-size: 56px; }
  .card--front .brand__dot { width: 40px; height: 40px; }

  .front-web {
    position: absolute;
    right: 60px;
    bottom: 50px;
    color: var(--gold);
    font-size: 22px;
    letter-spacing: 0.32em;
  }

  .back-panel {
    position: absolute;
    inset: 0;
    background: var(--card-white);
    clip-path: polygon(62% 0, 100% 0, 100% 100%, 42% 100%);
  }
  .card--back .brand { left: 70px; top: 150px; font-size: 32px; }
  .card--back .brand__dot { width: 24px; height: 24px; gap: 12px; }

  .contact {
    position: absolute;
    right: 40px;
    top: 40px;
    text-align: right;
    color: var(--gold);
  }
  .contact__name { font-size: 28px; font-weight: 600; }
  .contact__title { font-size: 20px; font-weight: 600; margin-top: 4px; }
  .contact__lines {
    position: absolute;
    right: 40px;
    bottom: 38px;
    text-align: right;
    color: var(--gold);
    font-size: 19px;
    line-height: 1.55;
  }
  .contact__lines .address { margin-top: 10px; }
</style>
</head>
<body>
  <section class="card card--front" aria-label="Card front">
    <div class="brand"><span class="brand__dot"></span>Solenne Sport</div>
    <div class="front-web">fieldlaneco.example</div>
  </section>

  <section class="card card--back" aria-label="Card back">
    <div class="brand"><span class="brand__dot"></span>Solenne Sport</div>
    <div class="back-panel"></div>
    <div class="contact">
      <div class="contact__name">Peter L. Vandrell</div>
      <div class="contact__title">CFB, CTB</div>
    </div>
    <div class="contact__lines">
      <div>C : +1 503.555.0147</div>
      <div>O : +1 808.555.0182</div>
      <div>E : Peter@fieldlaneco.example</div>
      <div>W : www.fieldlaneco.example</div>
      <div class="address">48317 W 63rd Ave Harlow Ridge, WA 99482</div>
    </div>
  </section>
</body>
</html>
```